Präsentationsvorlagen für Strahlenschutzkurse
Zielgruppe
Wir bieten Strahlenschutzkurse in der Medizin an. Zielgruppe: Ärztinnen und Ärzte
Stichworte: Erwachsenenbildung, wissenschaftliche Inhalte
Aufgabenstellung
Wir benötigen eine Power-Point Präsentationsvorlage für unsere Kurse.
Auf allen Folien:
*Integration von unserem Logo
*Übernahme unseres bestehenden Farbkonzepts
*Feld für Überschrift
*kleines Textfeld für die Angabe der jeweiligen Quelle
Wir benötigen:
eine Folie nur mit Textfeld (z.B. Aufzählung, kurzer Text)
eine Folie Text mit Bild
eine Folie Bild bzw. Video
eine Folie mit einem wichtigen Lehrinhalt (wichtiger Text) - besondere Vorhebung erwünscht
eine Folie für Anfang bzw. Ende
HEX-CODE:
#4f93fe
#eea62f
#ffffff

```html
<!DOCTYPE html>
<html lang="de">
<head>
<meta charset="utf-8">
<title>Präsentationsvorlage Strahlenschutzkurse</title>
<link href="https://fonts.googleapis.com/css2?family=Poppins:ital,wght@0,300;0,400;0,500;0,600;0,700;0,800;1,600&display=swap" rel="stylesheet">
<style>
  :root{
    --navy:#1a5479;
    --sky:#0096ff;
    --amber:#fda81b;
    --white:#ffffff;
    --stage:#9aa7b5;
    --tag:#9aa7b5;
  }
  *{margin:0;padding:0;box-sizing:border-box}
  html,body{width:1200px;height:1200px;overflow:hidden;background:var(--stage)}
  body{position:relative;font-family:'Poppins',sans-serif}
  .slide{position:absolute;width:750px;height:423px;background:var(--white);overflow:hidden;
    transform-origin:0 0;transform:scale(.6211);box-shadow:0 14px 12px -8px rgba(40,55,70,.35)}
  .s-cover{left:89px;top:133px}
  .s-textimage{left:645px;top:135px}
  .s-list{left:89px;top:469px}
  .s-stats{left:647px;top:469px}
  .s-photo{left:89px;top:802px}
  .s-headline{left:645px;top:802px}
  .block{position:absolute}
  .slide-title{position:absolute;left:62px;top:36px;font-weight:800;font-size:40px;color:var(--navy);letter-spacing:.5px}
  .body-copy{position:absolute;font-size:16px;line-height:19.4px;letter-spacing:1.3px;color:var(--navy);font-weight:400}
  .source-tag{position:absolute;right:0;bottom:2px;width:156px;height:14px;background:var(--tag);
    font-size:6.5px;font-style:italic;font-weight:600;letter-spacing:1.5px;color:var(--navy);text-align:center;line-height:14px}
  .brand{position:absolute;display:flex;align-items:center;gap:5px;color:var(--navy);font-weight:500;white-space:nowrap}
  .brand .dot{border-radius:50%;border:1.5px solid var(--navy)}
  .brand-small{left:12px;bottom:18px;font-size:7px;letter-spacing:.3px}
  .brand-small .dot{width:12px;height:12px}
  /* cover */
  .cover-photo{left:0;top:0;width:330px;height:423px;background:radial-gradient(ellipse 32% 40% at 48% 48%,#f5c21c 0,#f3bd22 70%,rgba(255,255,255,0) 100%),linear-gradient(#ffffff,#f2f2f2)}
  .cover-panel{left:330px;top:0;width:420px;height:330px;background:var(--navy)}
  .cover-band{left:330px;top:330px;width:420px;height:93px;background:var(--amber)}
  .cover-rule{left:410px;top:126px;width:3px;height:97px;background:var(--white)}
  .cover-kicker{left:431px;top:116px;font-size:32px;font-weight:400;color:var(--white)}
  .cover-title{left:431px;top:150px;font-size:40px;font-weight:800;color:var(--white)}
  .cover-tagline{left:431px;top:204px;font-size:14.5px;letter-spacing:1px;color:var(--white)}
  .cover-brand{left:458px;top:365px;font-size:13px;letter-spacing:.5px}
  .cover-brand .dot{width:26px;height:26px}
  /* text+image */
  .accent-bar{left:0;top:114px;width:106px;height:309px;background:var(--amber)}
  .hazmat-photo{left:106px;top:114px;width:279px;height:309px;background:linear-gradient(135deg,#e9ecef 0,#d9dde0 45%,#8c8883 75%,#6f6b66 100%)}
  /* list */
  .list-panel{left:374px;top:108px;width:376px;height:315px;background:var(--navy)}
  .list-item{position:absolute;left:408px;display:flex;gap:28px}
  .list-num{width:32px;height:32px;background:var(--amber);color:var(--white);font-size:12px;font-weight:500;display:flex;align-items:center;justify-content:center}
  .list-head{font-size:11.5px;font-weight:600;letter-spacing:2.2px;color:var(--white);margin-top:-2px}
  .list-sub{font-size:6.5px;font-weight:600;color:var(--amber);line-height:9px;margin-top:4px;letter-spacing:.3px}
  /* stats */
  .stats-panel{left:106px;top:112px;width:290px;height:311px;background:var(--navy)}
  .stat{position:absolute;width:110px;text-align:center}
  .stat-box{margin:0 auto;width:70px;height:68px;border:4px solid;border-image:linear-gradient(var(--amber) 58%,var(--sky) 58%) 1;
    display:flex;align-items:center;justify-content:center;font-size:19px;font-weight:700;color:var(--navy)}
  .stat-label{font-size:9.5px;font-weight:700;color:var(--navy);margin-top:6px}
  .stat-note{font-size:5.8px;color:var(--navy);line-height:8px;margin-top:2px;letter-spacing:.3px}
  /* photo headline */
  .warehouse-photo{left:0;top:0;width:750px;height:423px;background:radial-gradient(ellipse 30% 60% at 50% 35%,#6f8f8a 0,#3e5f5c 55%,rgba(0,0,0,0) 100%),linear-gradient(90deg,#7a7a1a 0,#4d5320 20%,#2f4a4a 45%,#2f4a4a 60%,#6b6d1c 85%,#9a9620 100%)}
  .photo-band{left:108px;top:278px;width:642px;height:145px;background:rgba(26,84,121,.55)}
  .photo-accent{left:0;top:278px;width:108px;height:145px;background:var(--amber)}
  .headline{position:absolute;width:100%;text-align:center;font-size:40px;font-weight:800;color:var(--white);letter-spacing:.3px}
  .headline-copy{position:absolute;width:100%;text-align:center;font-size:12.3px;line-height:15.5px;letter-spacing:1.2px;color:var(--white)}
  .s-photo .brand{color:var(--navy)}
  /* headline slide */
  .top-band{left:0;top:0;width:750px;height:145px;background:var(--navy)}
  .bottom-band{left:0;top:145px;width:750px;height:278px;background:var(--sky)}
  .faint-mark{left:62px;top:120px;font-size:18px;font-weight:600;color:#a9b3bd;letter-spacing:1px;display:flex;align-items:center;gap:8px}
  .faint-mark .dot{width:30px;height:30px;border:2px solid #a9b3bd;border-radius:50%}
  .feature{position:absolute;top:252px;width:140px;text-align:center;color:var(--white);font-size:12px;font-weight:600;letter-spacing:3px;line-height:16px}
  .feature svg{display:block;margin:0 auto 4px}
  .divider{position:absolute;top:255px;width:1px;height:66px;background:rgba(255,255,255,.45)}
  /* palette */
  .swatch{position:absolute;top:1114px;width:86px;height:59px;border:1.5px solid #1c2430}
</style>
</head>
<body>

<section class="slide s-cover">
  <div class="block cover-photo" role="img" aria-label="Foto: gelbes Fass mit Strahlenwarnzeichen"></div>
  <div class="block cover-panel"></div>
  <div class="block cover-band"></div>
  <div class="block cover-rule"></div>
  <div class="block cover-kicker">Here</div>
  <div class="block cover-title">MAIN TITLE</div>
  <div class="block cover-tagline">YOUR TAGLINE HERE</div>
  <div class="brand cover-brand"><span class="dot"></span>VELMAR STRAHLENKOLLEG</div>
</section>

<section class="slide s-textimage">
  <h2 class="slide-title">SLIDE TITLE</h2>
  <div class="block accent-bar"></div>
  <div class="block hazmat-photo" role="img" aria-label="Foto: Person im Schutzanzug mit Atemschutzmaske entnimmt eine Probe"></div>
  <p class="body-copy" style="left:443px;top:134px;width:290px">Lorem ipsum dolor sit amet, consectetuer adipiscing elit, sed diam nonummy nibh euismod tincidunt ut laoreet dolore magna aliquam erat volutpat. Ut wisi enim ad minim veniam, quis nostrud exerci tation ullamcorper suscipit lobortis nisl ut aliquip ex ea commodo consequat.</p>
  <div class="brand brand-small"><span class="dot"></span>VELMAR STRAHLENKOLLEG</div>
  <div class="source-tag">DATA LINKS</div>
</section>

<section class="slide s-list">
  <h2 class="slide-title">SLIDE TITLE</h2>
  <div class="block accent-bar" style="top:112px"></div>
  <p class="body-copy" style="left:140px;top:138px;width:216px;text-align:right">Lorem ipsum dolor sit amet, consectetuer adipiscing elit, sed diam nonummy nibh euismod tincidunt ut laoreet dolore magna aliquam erat volutpat. Ut wisi enim ad minim veniam, quis nostrud exerci tation ullamcorper suscipit lobortis nisl</p>
  <div class="block list-panel"></div>
  <div class="list-item" style="top:150px"><div class="list-num">01</div><div><div class="list-head">LOREM IPSUM DOLOR</div><div class="list-sub">Lorem ipsum dolor sit amet, consectetuer adipiscing<br>elit, sed diam nonummy nibh euismod tincidunt.</div></div></div>
  <div class="list-item" style="top:230px"><div class="list-num">02</div><div><div class="list-head">LOREM IPSUM DOLOR</div><div class="list-sub">Lorem ipsum dolor sit amet, consectetuer adipiscing<br>elit, sed diam nonummy nibh euismod tincidunt.</div></div></div>
  <div class="list-item" style="top:310px"><div class="list-num">03</div><div><div class="list-head">LOREM IPSUM DOLOR</div><div class="list-sub">Lorem ipsum dolor sit amet, consectetuer adipiscing<br>elit, sed diam nonummy nibh euismod tincidunt.</div></div></div>
  <div class="brand brand-small"><span class="dot"></span>VELMAR STRAHLENKOLLEG</div>
  <div class="source-tag">DATA LINKS</div>
</section>

<section class="slide s-stats">
  <h2 class="slide-title">SLIDE TITLE</h2>
  <div class="block accent-bar" style="top:112px"></div>
  <div class="block stats-panel"></div>
  <p class="body-copy" style="left:140px;top:198px;width:236px;text-align:center;color:var(--white)">Lorem ipsum dolor sit amet, consectetuer adipiscing elit, sed diam nonummy nibh euismod tincidunt ut laoreet dolore magna</p>
  <div class="stat" style="left:439px;top:138px"><div class="stat-box">43%</div><div class="stat-label">LOREM IPSUM</div><div class="stat-note">Lorem ipsum dolor sit<br>amet, consectetuer.</div></div>
  <div class="stat" style="left:603px;top:138px"><div class="stat-box">50%</div><div class="stat-label">LOREM IPSUM</div><div class="stat-note">Lorem ipsum dolor sit<br>amet, consectetuer.</div></div>
  <div class="stat" style="left:439px;top:276px"><div class="stat-box">25%</div><div class="stat-label">LOREM IPSUM</div><div class="stat-note">Lorem ipsum dolor sit<br>amet, consectetuer.</div></div>
  <div class="stat" style="left:603px;top:276px"><div class="stat-box">78%</div><div class="stat-label">LOREM IPSUM</div><div class="stat-note">Lorem ipsum dolor sit<br>amet, consectetuer.</div></div>
  <div class="brand brand-small"><span class="dot"></span>VELMAR STRAHLENKOLLEG</div>
  <div class="source-tag">DATA LINKS</div>
</section>

<section class="slide s-photo">
  <div class="block warehouse-photo" role="img" aria-label="Foto: Person im gelben Schutzanzug zwischen Reihen gelber Gefahrstofffässer in einer Lagerhalle"></div>
  <div class="block photo-band"></div>
  <div class="block photo-accent"></div>
  <div class="headline" style="left:0;top:292px;padding-left:0;width:740px">HEADLINE SLIDE</div>
  <p class="headline-copy" style="left:0;top:347px;width:740px">Lorem ipsum dolor sit amet, consectetuer<br>adipiscing elit, sed diam nonummy nibh<br>euismod tincidunt ut laoreet dolore magna</p>
  <div class="brand brand-small"><span class="dot"></span>VELMAR STRAHLENKOLLEG</div>
</section>

<section class="slide s-headline">
  <div class="block top-band"></div>
  <div class="block bottom-band"></div>
  <div class="headline" style="left:0;top:14px;width:740px">HEADLINE SLIDE</div>
  <p class="headline-copy" style="left:0;top:70px;width:752px">Lorem ipsum dolor sit amet, consectetuer<br>adipiscing elit, sed diam nonummy nibh<br>euismod tincidunt ut laoreet dolore magna</p>
  <div class="block faint-mark"><span class="dot"></span>VELMAR</div>
  <div class="feature" style="left:120px">
    <svg width="34" height="34" viewBox="0 0 34 34" fill="none" stroke="#fff" stroke-width="2"><circle cx="17" cy="17" r="14"/><ellipse cx="17" cy="17" rx="6" ry="14"/><line x1="3" y1="17" x2="31" y2="17"/><path d="M6 9h22M6 25h22"/></svg>
    LOREM IPSUM<br>DOLOR SIT</div>
  <div class="divider" style="left:281px"></div>
  <div class="feature" style="left:303px">
    <svg width="34" height="34" viewBox="0 0 34 34"><g fill="#fff"><circle cx="17" cy="17" r="10"/><g stroke="#fff" stroke-width="5"><line x1="17" y1="3" x2="17" y2="31"/><line x1="3" y1="17" x2="31" y2="17"/><line x1="7" y1="7" x2="27" y2="27"/><line x1="27" y1="7" x2="7" y2="27"/></g></g><circle cx="17" cy="17" r="4" fill="#0096ff"/></svg>
    LOREM IPSUM<br>DOLOR SIT</div>
  <div class="divider" style="left:464px"></div>
  <div class="feature" style="left:486px">
    <svg width="34" height="34" viewBox="0 0 34 34"><rect x="13" y="6" width="8" height="6" fill="none" stroke="#fff" stroke-width="2.5"/><rect x="3" y="11" width="28" height="19" rx="2" fill="#fff"/></svg>
    LOREM IPSUM<br>DOLOR SIT</div>
  <div class="source-tag">DATA LINKS</div>
</section>

<div class="swatch" style="left:412px;background:var(--navy)"></div>
<div class="swatch" style="left:509px;background:var(--sky)"></div>
<div class="swatch" style="left:605px;background:var(--amber)"></div>
<div class="swatch" style="left:701px;background:var(--stage)"></div>

</body>
</html>
```